Business Card Design

We are a radiology group

We are working to move into new service centers

We want to communicate innovation and bringing our customers ahead with technology and outstanding results
Updates

I have uploaded a high resolution logo as requested :-)

Target Market(s)

hospitals, clinics

Industry/Entity Type

Business

Contact Information for Business Card

Deborah L. Pettigrew, MBA, CIIP
CTIO
deborah.pettigrew@tdrpc-mail.com
cell 518-476-2913
www.tdrpc-mail.com
Tidewater Diagnostic Radiology, PC

```html
<!DOCTYPE html>
<html lang="en">
<head>
<meta charset="utf-8">
<title>Business Card – Tidewater Diagnostic Radiology</title>
<link rel="stylesheet" href="https://fonts.googleapis.com/css2?family=Arimo:wght@400;700&display=swap">
<style>
  :root {
    --bg: #d9d9db;
    --card: #fbfbfb;
    --brand-blue: #1a7fd0;
    --ink: #1b1b1b;
    --logo-grey: #4a4a4a;
    --photo-dark: #0f1c33;
    --photo-mid: #3a5a8c;
    --photo-light: #c9b9a6;
  }
  * { margin: 0; padding: 0; box-sizing: border-box; }
  html, body {
    width: 1200px; height: 1011px; overflow: hidden;
    background: var(--bg);
    font-family: "Arimo", Arial, sans-serif;
  }
  .card {
    position: absolute;
    left: 350px; top: 68px;
    width: 500px; height: 875px;
    background: var(--card);
    box-shadow: 0 10px 30px rgba(0,0,0,0.18);
    overflow: hidden;
  }
  .brand {
    position: absolute;
    left: 50px; top: 95px;
    width: 400px;
    display: flex; align-items: center; gap: 20px;
  }
  .brand-dot {
    width: 44px; height: 44px; border-radius: 50%;
    background: var(--brand-blue);
    flex: none;
  }
  .brand-name {
    color: var(--logo-grey);
    font-weight: 700;
    font-size: 31px;
    line-height: 1.25;
    letter-spacing: 2px;
    text-transform: uppercase;
  }
  .holder {
    position: absolute;
    left: 60px; top: 300px;
    color: var(--brand-blue);
  }
  .holder-name { font-size: 27px; font-weight: 700; }
  .holder-creds { font-size: 24px; font-weight: 400; margin-top: 8px; padding-left: 28px; }
  .contacts {
    position: absolute;
    left: 70px; top: 405px;
    list-style: none;
    color: var(--ink);
  }
  .contacts li {
    display: flex; align-items: center; gap: 14px;
    font-size: 22px;
    height: 44px;
  }
  .contacts li.phone { font-size: 25px; }
  .contact-icon { width: 26px; height: 26px; flex: none; }
  .photo {
    position: absolute;
    left: 0; top: 560px;
    width: 500px; height: 250px;
    background: linear-gradient(110deg, var(--photo-light) 0%, var(--photo-mid) 35%, var(--photo-dark) 65%, var(--photo-mid) 100%);
  }
  .company-band {
    position: absolute;
    left: 0; bottom: 0;
    width: 500px; height: 65px;
    background: var(--brand-blue);
    color: #fff;
    font-size: 22px;
    display: flex; align-items: center; justify-content: flex-end;
    padding-right: 26px;
  }
</style>
</head>
<body>
  <article class="card">
    <div class="brand">
      <span class="brand-dot"></span>
      <span class="brand-name">Tidewater<br>Diagnostic<br>Radiology</span>
    </div>

    <div class="holder">
      <div class="holder-name">Deborah L. Pettigrew</div>
      <div class="holder-creds">MBA | CIIP CTIO</div>
    </div>

    <ul class="contacts">
      <li class="phone">
        <svg class="contact-icon" viewBox="0 0 26 26" aria-hidden="true">
          <circle cx="13" cy="13" r="13" fill="var(--brand-blue)"/>
          <rect x="9" y="6" width="8" height="14" rx="1.5" fill="#fff"/>
          <rect x="10.3" y="8" width="5.4" height="8.5" fill="var(--brand-blue)"/>
        </svg>
        518-476-2913
      </li>
      <li class="email">
        <svg class="contact-icon" viewBox="0 0 26 26" aria-hidden="true">
          <circle cx="13" cy="13" r="13" fill="var(--brand-blue)"/>
          <rect x="6.5" y="8.5" width="13" height="9" fill="#fff"/>
          <path d="M6.5 8.5 L13 13.5 L19.5 8.5" fill="none" stroke="var(--brand-blue)" stroke-width="1.3"/>
        </svg>
        deborah.pettigrew@tdrpc-mail.com
      </li>
      <li class="web">
        <svg class="contact-icon" viewBox="0 0 26 26" aria-hidden="true">
          <circle cx="13" cy="13" r="13" fill="var(--brand-blue)"/>
          <circle cx="13" cy="13" r="7" fill="none" stroke="#fff" stroke-width="1.5"/>
          <ellipse cx="13" cy="13" rx="3" ry="7" fill="none" stroke="#fff" stroke-width="1.3"/>
          <line x1="6" y1="13" x2="20" y2="13" stroke="#fff" stroke-width="1.3"/>
        </svg>
        www.tdrpc-mail.com
      </li>
    </ul>

    <div class="photo" role="img" aria-label="Photo of a radiologist reviewing imaging scans on a screen with a patient"></div>

    <div class="company-band">Tidewater Diagnostic Radiology, PC</div>
  </article>
</body>
</html>
```